Emerging jewellery maker and designer needs a business card design with logo

I need a business card to hand to industry officials and potential clients. I handmake my own jewellery that targets mostly females from 20 to 50 years of age. I use mostly sterling silver, with some gemstones and often have tribal or geometric elements in the design. The final design should communicate originality, simplicity and memorability.

Target Market(s)

20- 50 year old females

Industry/Entity Type

Business

Contact Information for Business Card

Title: Marisol Quenton Designs
Tagline: Jewellery and Object maker
Contact details:
-email: kmquenton4@mailvora.com
-instagram: @marisolquenton
-Mobile: 047-612-5093

Requirements
Must have
• Clear and strong design aesthetic
Nice to have
• I like symbols and use tribal and geometric symbols in my work. If this could be incorporated that would be great.( ideally a way better/digital version of the uploaded image could act as a logo of sorts)
Should not have
• Tacky sayings or quotes, misleading images, or an literal images of diamonds, rings etc

```html
<!DOCTYPE html>
<html lang="en">
<head>
<meta charset="UTF-8">
<title>Marisol Quenton Designs – Business Card</title>
<link rel="stylesheet" href="https://fonts.googleapis.com/css2?family=Open+Sans:wght@300;400&display=swap">
<style>
  :root {
    --page: #ffffff;
    --card: #050505;
    --teal: #3aa99d;
    --teal-deep: #1f6f68;
    --white: #f2f2f2;
    --corner: #3a3a3a;
    --corner-edge: #1a1a1a;
  }
  * { margin: 0; padding: 0; box-sizing: border-box; }
  html, body {
    width: 800px; height: 1200px; overflow: hidden;
    background: var(--page);
    font-family: "Open Sans", "Segoe UI", sans-serif;
    font-weight: 300;
  }
  .canvas { position: relative; width: 800px; height: 1200px; }

  .card {
    position: absolute; left: 8px; width: 784px; height: 465px;
    background: var(--card); overflow: hidden;
  }
  .card--front { top: 116px; }
  .card--back { top: 616px; }

  .corner {
    position: absolute; width: 130px; height: 130px; border-radius: 50%;
    background: radial-gradient(circle at 50% 50%, var(--corner) 0%, var(--corner-edge) 100%);
  }
  .corner--top-left { left: -65px; top: -65px; }
  .corner--bottom-right { right: -65px; bottom: -65px; }

  .brand { position: absolute; text-align: center; }
  .brand__name {
    color: var(--teal); font-weight: 300; letter-spacing: 0.5px; line-height: 1;
  }
  .brand__suffix {
    color: var(--teal); font-weight: 400; letter-spacing: 1px; line-height: 1;
  }
  .brand__tagline { color: var(--white); font-weight: 300; line-height: 1; }

  .card--front .brand { left: 40px; width: 340px; top: 192px; }
  .card--front .brand__name { font-size: 36px; }
  .card--front .brand__suffix { font-size: 17px; margin-top: 6px; }
  .card--front .brand__tagline { font-size: 19px; margin-top: 10px; }

  .divider {
    position: absolute; left: 392px; top: 112px; width: 2px; height: 305px;
    background: linear-gradient(var(--teal-deep), var(--teal), var(--teal-deep));
  }

  .contacts { position: absolute; left: 422px; top: 153px; list-style: none; }
  .contact {
    display: flex; align-items: center; height: 44px; margin-bottom: 15px;
    color: var(--white); font-size: 21px;
  }
  .contact__icon { width: 42px; height: 42px; margin-right: 12px; flex: none; }

  .mark { position: absolute; left: 342px; top: 82px; width: 100px; height: 100px; }
  .card--back .brand { left: 0; width: 784px; top: 284px; }
  .card--back .brand__name { font-size: 40px; }
  .card--back .brand__suffix { font-size: 18px; margin-top: 4px; }
  .card--back .brand__tagline { font-size: 20px; margin-top: 12px; }
</style>
</head>
<body>
<main class="canvas">

  <section class="card card--front" aria-label="Business card front">
    <span class="corner corner--top-left"></span>
    <span class="corner corner--bottom-right"></span>

    <div class="brand">
      <p class="brand__name">Marisol Quenton</p>
      <p class="brand__suffix">DESIGNS</p>
      <p class="brand__tagline">jewellery and object maker</p>
    </div>

    <span class="divider"></span>

    <ul class="contacts">
      <li class="contact">
        <svg class="contact__icon" viewBox="0 0 42 42" aria-hidden="true">
          <circle cx="21" cy="21" r="19" fill="none" stroke="var(--teal)" stroke-width="2.5"/>
          <path d="M14 12c1.5-1.5 3-1 4 .5l1.5 2.5c.8 1.3.3 2.4-.8 3.2-.8.6-.9 1.3-.3 2.4 1.2 2 2.4 3.2 4.4 4.4 1.1.6 1.8.5 2.4-.3.8-1.1 1.9-1.6 3.2-.8l2.5 1.5c1.5 1 2 2.5.5 4-2 2-5 2.3-8.5.2-3.5-2-6.3-4.8-8.3-8.3C11.7 17 12 14 14 12z" fill="var(--teal)"/>
        </svg>
        <span class="contact__text">047-612-5093</span>
      </li>
      <li class="contact">
        <svg class="contact__icon" viewBox="0 0 42 42" aria-hidden="true">
          <circle cx="21" cy="21" r="19" fill="var(--teal)"/>
          <rect x="11" y="14" width="20" height="14" rx="1.5" fill="var(--card)"/>
          <path d="M11.5 14.8 21 22l9.5-7.2" fill="none" stroke="var(--teal)" stroke-width="1.8"/>
        </svg>
        <span class="contact__text">kmquenton4@mailvora.com</span>
      </li>
      <li class="contact">
        <svg class="contact__icon" viewBox="0 0 42 42" aria-hidden="true">
          <circle cx="21" cy="21" r="19" fill="var(--teal)"/>
        </svg>
        <span class="contact__text">@marisolquenton</span>
      </li>
    </ul>
  </section>

  <section class="card card--back" aria-label="Business card back">
    <svg class="mark" viewBox="0 0 100 100" aria-hidden="true">
      <circle cx="50" cy="50" r="44" fill="none" stroke="var(--teal)" stroke-width="4"/>
    </svg>
    <div class="brand">
      <p class="brand__name">Marisol Quenton</p>
      <p class="brand__suffix">DESIGNS</p>
      <p class="brand__tagline">jewellery and object maker</p>
    </div>
  </section>

</main>
</body>
</html>
```